Business Card Design Project

Refresh of logo attached. Require text underneath to be more ledgible, crisper & cleaner.

Overall, staying with same colour scheme need a brighter, crisper, easily readible business card style.

Industry/Entity Type

Business

```html
<!DOCTYPE html>
<html lang="en">
<head>
<meta charset="utf-8">
<title>Elmora Business Card</title>
<link href="https://fonts.googleapis.com/css2?family=Belleza&display=swap" rel="stylesheet">
<style>
  :root {
    --backdrop: #c6c6c6;
    --card: #ffffff;
    --ink: #3a3838;
    --ink-soft: #2a2a2a;
    --teal: #217ea0;
    --slate: #2c5062;
    --icon: #1f5f8b;
    --pattern-light: #c3cdcf;
    --pattern-mid: #b1b6b2;
    --cream: #f8f8e8;
  }
  * { box-sizing: border-box; margin: 0; padding: 0; }
  html, body {
    width: 1200px; height: 900px; overflow: hidden;
    background: var(--backdrop);
    font-family: "Belleza", "Helvetica Neue", sans-serif;
    color: var(--ink);
  }
  .canvas { position: relative; width: 1200px; height: 900px; }

  .card { position: absolute; left: 313px; width: 637px; height: 368px; overflow: hidden; }
  .card-front { top: 55px; }
  .card-back { top: 476px; background: var(--card); }

  .front-pattern {
    position: absolute; inset: 0;
    background: linear-gradient(135deg, var(--pattern-light) 0%, var(--cream) 50%, var(--pattern-mid) 100%);
  }

  .brand { position: absolute; display: flex; align-items: center; white-space: nowrap; }
  .brand-square { background: var(--teal); flex: none; }
  .brand-name { color: var(--ink); line-height: 1; letter-spacing: 0.5px; }

  .card-front .brand { right: 30px; top: 222px; gap: 16px; }
  .card-front .brand-square { width: 54px; height: 54px; }
  .card-front .brand-name { font-size: 52px; }

  .card-back .brand { left: 57px; top: 54px; gap: 14px; }
  .card-back .brand-square { width: 56px; height: 56px; }
  .card-back .brand-name { font-size: 52px; }

  .band { position: absolute; left: 0; top: 128px; width: 637px; height: 41px; display: flex; }
  .band-accent { width: 114px; background: var(--slate); }
  .band-main {
    flex: 1; background: var(--teal); color: #fff;
    font-size: 14.5px; letter-spacing: 1.1px; text-transform: uppercase;
    padding-left: 13px; display: flex; align-items: center; white-space: nowrap;
  }

  .person { position: absolute; left: 127px; top: 216px; color: var(--ink-soft); }
  .person-name { font-size: 21px; line-height: 1.2; }
  .person-title { font-size: 16px; line-height: 1.3; }

  .contacts {
    position: absolute; left: 127px; top: 279px;
    display: grid; grid-template-columns: 164px auto; row-gap: 5px;
    font-size: 16.5px; color: var(--ink-soft);
  }
  .contact { display: flex; align-items: center; gap: 6px; white-space: nowrap; }
  .contact-icon { width: 14px; height: 14px; flex: none; }
  .contact:nth-child(even) { gap: 12px; }
</style>
</head>
<body>
<main class="canvas">
  <section class="card card-front">
    <div class="front-pattern" role="img" aria-label="Repeating geometric cube pattern in pale blue-grey, grey and cream"></div>
    <div class="brand">
      <span class="brand-square"></span>
      <span class="brand-name">ELMORA</span>
    </div>
  </section>

  <section class="card card-back">
    <div class="brand">
      <span class="brand-square"></span>
      <span class="brand-name">ELMORA</span>
    </div>
    <div class="band">
      <div class="band-accent"></div>
      <div class="band-main">Elmora Institute of Estate Executor Advisors</div>
    </div>
    <div class="person">
      <p class="person-name">Peter L.Harwood</p>
      <p class="person-title">Certified Executor Advisor</p>
    </div>
    <div class="contacts">
      <div class="contact">
        <svg class="contact-icon" viewBox="0 0 14 14" aria-hidden="true"><circle cx="7" cy="7" r="7" fill="var(--icon)"/><path d="M3.5 7.2 7 4l3.5 3.2H9.5V10h-5V7.2z" fill="#fff"/></svg>
        <span>(416) 555 0142</span>
      </div>
      <div class="contact">
        <svg class="contact-icon" viewBox="0 0 14 14" aria-hidden="true"><circle cx="7" cy="7" r="7" fill="var(--icon)"/><path d="M4.3 3.6c.4-.3.9-.3 1.1.1l.7 1.2c.2.4 0 .7-.3.9l-.4.3c.4 1 1.2 1.8 2.2 2.2l.3-.4c.2-.3.6-.5.9-.3l1.2.7c.4.2.4.7.1 1.1-.6.8-1.5.9-2.4.5-1.7-.7-3-2-3.7-3.7-.4-.9-.3-1.8.3-2.6z" fill="#fff"/></svg>
        <span>(647) 555 0178</span>
      </div>
      <div class="contact">
        <svg class="contact-icon" viewBox="0 0 14 14" aria-hidden="true"><circle cx="7" cy="7" r="7" fill="var(--icon)"/><rect x="3.5" y="4.5" width="7" height="5" fill="#fff"/><path d="M3.5 4.5 7 7.3l3.5-2.8" fill="none" stroke="var(--icon)" stroke-width=".8"/></svg>
        <span>peter@elmora.ca</span>
      </div>
      <div class="contact">
        <svg class="contact-icon" viewBox="0 0 14 14" aria-hidden="true"><circle cx="7" cy="7" r="7" fill="var(--icon)"/><circle cx="7" cy="7" r="4" fill="none" stroke="#fff" stroke-width=".9"/><path d="M3 7h8M7 3c-1.6 2.4-1.6 5.6 0 8M7 3c1.6 2.4 1.6 5.6 0 8" fill="none" stroke="#fff" stroke-width=".8"/></svg>
        <span>www.elmora.ca</span>
      </div>
    </div>
  </section>
</main>
</body>
</html>
```